How likely are people to engage in social distancing? We need a good illustration to show the data!

We surveyed U.S. adults March 20th - 24th, 2020 and asked how likely they were to engage in social distancing (and other COVID-19 related health behaviors). What did the survey find? Basically, most people intend to engage in social distancing behaviors (e.g., avoiding large crowds) and other behaviors that reduce the spread of COVID-19 (e.g., washing hands at least 20 seconds). When most people intend to engage in a behavior, then public health professionals try to leverage that to move more people to act.
Now we need innovative and professional images that attempt to communicate one or all of these findings. The specific findings are nicely summarized in the attached document. For example, 82% of participants intend to engage in social distancing.
What sort of visual are we looking for? Our preference is for an original illustration (or set of illustrations). Our preference is for (creative and powerful illustrations, but we are also open to the creative and well-executed infographics.
We need these images fast . We will award monetary prizes to the 3 best designs. If we like more than that, then we might purchase more (e.g., in past contests, we have purchased as many as 30 designs).
What we will need:
(1) The illustrations must be original and we will need the photoshop and/or illustrator files for all artwork.
(2) You can illustrate all of the findings or just one of them. We need creative approaches that do a lucid job of bringing the data to life. Most people intend to engage in these behaviors. How to communicate that? Tollvarists and Brenmorites do not differ in their intentions; how to communicate that?
(3) The illustration should say, somewhere: "Based on a survey of 400 U.S. adults conducted March 20 - 24th, 2020."

Target Market(s)

U.S. Adults

Requirements
Must have
• Original illustrations based on the findings of the survey (see attached document).

```html
<!DOCTYPE html>
<html lang="en">
<head>
<meta charset="utf-8">
<title>Social Distancing Intentions</title>
<link href="https://fonts.googleapis.com/css2?family=Roboto+Condensed:wght@400;700&display=swap" rel="stylesheet">
<style>
  :root {
    --green: #8cc864;
    --red: #d41f43;
    --blue: #3d85c6;
    --grey: #bcbdc0;
    --icon: #6d6e71;
    --ink: #2b2b2b;
    --paper: #ffffff;
  }
  * { box-sizing: border-box; margin: 0; padding: 0; }
  html, body { width: 760px; height: 1200px; overflow: hidden; background: var(--paper); }
  body { font-family: "Roboto Condensed", "Arial Narrow", sans-serif; color: var(--ink); position: relative; }

  .headline {
    position: absolute; top: 34px; left: 0; width: 760px;
    text-align: center; font-size: 22px; line-height: 30px; font-weight: 400;
  }

  .behaviors { position: absolute; top: 129px; left: 0; width: 760px; height: 190px; }
  .behavior { position: absolute; top: 0; width: 90px; text-align: center; }
  .behavior .tag { display: block; margin: 0 auto; width: 76px; height: 61px; }
  .behavior .tag text { fill: #fff; font-size: 21px; font-weight: 700; font-family: "Roboto Condensed", sans-serif; }
  .behavior .icon {
    display: block; margin: 10px auto 0; width: 46px; height: 46px;
    background: var(--icon); border-radius: 50%; opacity: .85;
  }
  .behavior .label { margin-top: 16px; font-size: 11.5px; line-height: 13px; color: #444; font-weight: 700; }

  .summary {
    position: absolute; top: 325px; left: 30px; width: 702px; height: 33px;
    background: var(--green); color: #fff; font-size: 22px; font-weight: 700;
    display: flex; align-items: center; justify-content: center; gap: 8px;
  }

  .compare-title {
    position: absolute; top: 402px; left: 0; width: 760px; text-align: center;
    font-size: 30px; font-weight: 700; color: #333;
  }
  .compare-title .party-a { color: var(--red); }
  .compare-title .party-b { color: var(--blue); }
  .shield { position: absolute; top: 394px; width: 56px; height: 60px; }
  .shield.left { left: 44px; }
  .shield.right { left: 671px; }

  .chart { position: absolute; top: 481px; left: 37px; width: 684px; }
  .row { position: relative; height: 23px; margin-bottom: 7.8px; }
  .bar { position: absolute; top: 0; height: 23px; width: 334px; background: var(--grey); overflow: hidden; }
  .bar.a { left: 0; }
  .bar.b { left: 350px; }
  .fill { position: absolute; top: 0; height: 100%; }
  .bar.a .fill { left: 0; background: var(--red); }
  .bar.b .fill { right: 0; background: var(--blue); }
  .bar .name { position: absolute; left: 4px; top: 0; line-height: 23px; color: #fff; font-size: 14px; font-weight: 700; white-space: nowrap; }
  .bar .pct { position: absolute; top: 0; line-height: 23px; color: #fff; font-size: 19px; font-weight: 700; }
  .bar.a .pct { right: 2px; }
  .bar.b .pct { left: 3px; }

  .verdict { position: absolute; top: 760px; left: 0; width: 760px; text-align: center; font-size: 28px; font-weight: 700; line-height: 34px; }
  .verdict .a { color: var(--red); }
  .verdict .b { color: var(--blue); }

  .unity-art {
    position: absolute; top: 830px; left: 0; width: 760px; height: 310px;
    background: linear-gradient(100deg, var(--red) 0%, var(--red) 45%, var(--blue) 55%, var(--blue) 100%);
    opacity: .9;
  }

  .source { position: absolute; top: 1158px; left: 0; width: 760px; text-align: center; font-size: 15px; color: #222; }
</style>
</head>
<body>

<h1 class="headline">Percent of Americans intending to engage in social distancing<br>and perform these behaviors to slow the spread of coronavirus</h1>

<section class="behaviors">
  <div class="behavior" style="left:23px">
    <svg class="tag" viewBox="0 0 76 61"><polygon points="0,0 76,0 76,47 38,61 0,47" fill="var(--green)"/><text x="38" y="34" text-anchor="middle">82%</text></svg>
    <span class="icon" role="img" aria-label="Two people standing apart"></span>
    <p class="label">Engage<br>In Social<br>Distancing</p>
  </div>
  <div class="behavior" style="left:109px">
    <svg class="tag" viewBox="0 0 76 61"><polygon points="0,0 76,0 76,47 38,61 0,47" fill="var(--green)"/><text x="38" y="34" text-anchor="middle">63%</text></svg>
    <span class="icon" role="img" aria-label="House"></span>
    <p class="label">Work<br>From<br>Home</p>
  </div>
  <div class="behavior" style="left:195px">
    <svg class="tag" viewBox="0 0 76 61"><polygon points="0,0 76,0 76,47 38,61 0,47" fill="var(--green)"/><text x="38" y="34" text-anchor="middle">85%</text></svg>
    <span class="icon" role="img" aria-label="Crowd crossed out"></span>
    <p class="label">Avoid<br>Large<br>Gatherings</p>
  </div>
  <div class="behavior" style="left:283px">
    <svg class="tag" viewBox="0 0 76 61"><polygon points="0,0 76,0 76,47 38,61 0,47" fill="var(--green)"/><text x="38" y="34" text-anchor="middle">81%</text></svg>
    <span class="icon" role="img" aria-label="Calendar with cancelled date"></span>
    <p class="label">Cancel<br>Social<br>Activities</p>
  </div>
  <div class="behavior" style="left:374px">
    <svg class="tag" viewBox="0 0 76 61"><polygon points="0,0 76,0 76,47 38,61 0,47" fill="var(--green)"/><text x="38" y="34" text-anchor="middle">85%</text></svg>
    <span class="icon" role="img" aria-label="Two people with distance arrow"></span>
    <p class="label">Put Distance<br>Between Yourself<br>And Other<br>People</p>
  </div>
  <div class="behavior" style="left:465px">
    <svg class="tag" viewBox="0 0 76 61"><polygon points="0,0 76,0 76,47 38,61 0,47" fill="var(--green)"/><text x="38" y="34" text-anchor="middle">87%</text></svg>
    <span class="icon" role="img" aria-label="Hands being washed"></span>
    <p class="label">Wash<br>hands<br>at least 20</p>
  </div>
  <div class="behavior" style="left:556px">
    <svg class="tag" viewBox="0 0 76 61"><polygon points="0,0 76,0 76,47 38,61 0,47" fill="var(--green)"/><text x="38" y="34" text-anchor="middle">85%</text></svg>
    <span class="icon" role="img" aria-label="Hand sanitizer bottle"></span>
    <p class="label">Use<br>hand<br>sanitizer</p>
  </div>
  <div class="behavior" style="left:648px">
    <svg class="tag" viewBox="0 0 76 61"><polygon points="0,0 76,0 76,47 38,61 0,47" fill="var(--green)"/><text x="38" y="34" text-anchor="middle">81%</text></svg>
    <span class="icon" role="img" aria-label="No touching face symbol"></span>
    <p class="label">Avoid<br>touching<br>your eyes, nose</p>
  </div>
</section>

<div class="summary">
  <svg width="20" height="16" viewBox="0 0 20 16"><polyline points="2,8 7,13 18,2" fill="none" stroke="#fff" stroke-width="3.5"/></svg>
  Most people intend to engage in these behaviors.
</div>

<svg class="shield left" viewBox="0 0 56 60"><path d="M28 2 C20 8 10 10 2 10 C2 34 10 50 28 58 C46 50 54 34 54 10 C46 10 36 8 28 2Z" fill="var(--red)"/><path d="M28 9 C22 13 15 15 9 15 C9 34 16 46 28 52 C40 46 47 34 47 15 C41 15 34 13 28 9Z" fill="none" stroke="#fff" stroke-width="2"/></svg>
<svg class="shield right" viewBox="0 0 56 60"><path d="M28 2 C20 8 10 10 2 10 C2 34 10 50 28 58 C46 50 54 34 54 10 C46 10 36 8 28 2Z" fill="var(--blue)"/><path d="M28 9 C22 13 15 15 9 15 C9 34 16 46 28 52 C40 46 47 34 47 15 C41 15 34 13 28 9Z" fill="none" stroke="#fff" stroke-width="2"/></svg>

<h2 class="compare-title">Comparing <span class="party-a">Tollvarists</span> and <span class="party-b">Brenmorites</span></h2>

<section class="chart">
  <div class="row"><div class="bar a"><div class="fill" style="width:274px"></div><span class="name">Engage In Social Distancing</span><span class="pct">82%</span></div><div class="bar b"><div class="fill" style="width:271px"></div><span class="pct">81%</span></div></div>
  <div class="row"><div class="bar a"><div class="fill" style="width:200px"></div><span class="name">Work From Home</span><span class="pct">60%</span></div><div class="bar b"><div class="fill" style="width:214px"></div><span class="pct">65%</span></div></div>
  <div class="row"><div class="bar a"><div class="fill" style="width:284px"></div><span class="name">Avoid Large Gatherings</span><span class="pct">85%</span></div><div class="bar b"><div class="fill" style="width:282px"></div><span class="pct">84%</span></div></div>
  <div class="row"><div class="bar a"><div class="fill" style="width:274px"></div><span class="name">Cancel Social Activities</span><span class="pct">82%</span></div><div class="bar b"><div class="fill" style="width:270px"></div><span class="pct">80%</span></div></div>
  <div class="row"><div class="bar a"><div class="fill" style="width:281px"></div><span class="name">Put Distance Between Yourself And Other People</span><span class="pct">84%</span></div><div class="bar b"><div class="fill" style="width:291px"></div><span class="pct">87%</span></div></div>
  <div class="row"><div class="bar a"><div class="fill" style="width:290px"></div><span class="name">Wash Hands At Least 20 Seconds</span><span class="pct">87%</span></div><div class="bar b"><div class="fill" style="width:292px"></div><span class="pct">88%</span></div></div>
  <div class="row"><div class="bar a"><div class="fill" style="width:290px"></div><span class="name">Use Hand Sanitizer</span><span class="pct">87%</span></div><div class="bar b"><div class="fill" style="width:282px"></div><span class="pct">84%</span></div></div>
  <div class="row"><div class="bar a"><div class="fill" style="width:267px"></div><span class="name">Avoid Touching Your Eyes, Nose, And Mouth</span><span class="pct">80%</span></div><div class="bar b"><div class="fill" style="width:274px"></div><span class="pct">82%</span></div></div>
</section>

<div class="unity-art" role="img" aria-label="Red and blue arms meeting in a handshake"></div>

<p class="verdict"><span class="a">No big differences.</span><br><span class="b">Basically the same patterns.</span></p>

<p class="source">Based on a survey of 400 U.S. adults conducted March 20 - 24th, 2020.</p>

</body>
</html>
```